Emerging Australian photographer

I'm based in Cunderdin, a small rural town in the Wheatbelt area of Western Australia. So its a good thing that I love to travel further afield both for pleasure and for work. To me that is one and the same thing in any event!

My desire is to take photos that make the viewers heart skip. I love taking photos of people doing the things they love or being with the people they love. For me, the joy of photography comes with capturing the 'moments between the moments'. I like candid photography best of all - like when the new husband is staring joyfully at his bride and at that minute is unaware of the photographer capturing the moment.

I am available for weddings, engagements, birthdays, special events, newborns, family or individual portraits. By the end of the year I will be accredited with the Southern Guild of Practising Imagemakers.

I need a card that stands out but is elegant and would sit well on the table at a wedding or be given out in the church grounds. Classy and a little bit sassy.

Target Market(s)

Consumers who are seeking photographic services, eg wedding guests who see me at work and make enquiries.

Industry/Entity Type

Church

Contact Information for Business Card

Danielle Whitcombe Photography
Danielle Whitcombe
0438 562 073
www.daniellewhitcombe.com.au
photos@daniellewhitcombe.com.au

Requirements
Must have
• Must fit with the theme in the watermarks, but be crisp and modern.
Nice to have
• However it's not essential to have the pink! Chatterbook and Pipsqueak logos.
Should not have
• Old style fonts like times new roman.

```html
<!DOCTYPE html>
<html lang="en">
<head>
<meta charset="utf-8">
<title>Danielle Whitcombe Photography — Business Card</title>
<link rel="stylesheet" href="https://fonts.googleapis.com/css2?family=Open+Sans:wght@400;600&display=swap">
<style>
  :root {
    --canvas: #f2efec;
    --pink: #e9509d;
    --pink-pattern: #e44f99;
    --pink-light: #f28cbf;
    --white: #ffffff;
    --grey: #6f6f73;
    --grey-line: #8a8a8e;
  }
  * { box-sizing: border-box; margin: 0; padding: 0; }
  html, body {
    width: 1200px; height: 1000px; overflow: hidden;
    background: var(--canvas);
    font-family: "Open Sans", Arial, sans-serif;
  }
  .sheet {
    position: relative; width: 1200px; height: 1000px;
    display: flex; flex-direction: column; align-items: center; justify-content: center; gap: 60px;
  }
  .card {
    position: relative; width: 735px; height: 420px;
    box-shadow: 0 6px 18px rgba(0,0,0,0.18);
    overflow: hidden;
  }
  .card__art { position: absolute; inset: 0; width: 100%; height: 100%; }
  .frame-band { fill: var(--white); stroke: var(--pink-light); stroke-width: 16; }

  /* Front */
  .card--front .card__bg { fill: var(--pink); }
  .brand-name {
    position: absolute; left: 0; right: 0; top: 186px;
    text-align: center; color: var(--pink);
    font-size: 34px; font-weight: 400; letter-spacing: 0.5px;
    white-space: nowrap;
  }

  /* Back */
  .card--back .card__bg { fill: var(--pink-pattern); }
  .identity {
    position: absolute; right: 385px; top: 232px;
    text-align: right; white-space: nowrap;
  }
  .identity__name { color: var(--pink); font-size: 26px; font-weight: 400; line-height: 1.2; }
  .identity__role { color: var(--grey); font-size: 20px; line-height: 1.3; padding-right: 40px; }

  .contact { position: absolute; left: 400px; top: 150px; list-style: none; white-space: nowrap; }
  .contact__item { color: var(--grey); font-size: 15px; height: 42px; line-height: 42px; }

  .social {
    position: absolute; right: 90px; top: 116px;
    display: flex; gap: 10px; white-space: nowrap;
  }
  .social__item { display: flex; align-items: center; gap: 4px; color: var(--pink); font-size: 10px; line-height: 1; }
  .social__dot { width: 9px; height: 9px; border-radius: 50%; background: var(--pink); flex: none; }
  .icon-stroke { fill: none; stroke: var(--grey-line); stroke-width: 2; }
  .icon-fill { fill: var(--grey-line); }
</style>
</head>
<body>
<main class="sheet">

  <section class="card card--front" aria-label="Business card front">
    <svg class="card__art" viewBox="0 0 700 400" aria-hidden="true">
      <rect class="card__bg" width="700" height="400"/>
      <path class="frame-band" d="M105,58 H245 C285,58 300,36 350,36 C400,36 415,58 455,58 H595 A46,46 0 0 0 641,104 V160 C641,185 655,190 655,200 C655,210 641,215 641,240 V296 A46,46 0 0 0 595,342 H455 C415,342 400,364 350,364 C300,364 285,342 245,342 H105 A46,46 0 0 0 59,296 V240 C59,215 45,210 45,200 C45,190 59,185 59,160 V104 A46,46 0 0 0 105,58 Z"/>
    </svg>
    <p class="brand-name">Danielle Whitcombe Photography</p>
  </section>

  <section class="card card--back" aria-label="Business card back">
    <svg class="card__art" viewBox="0 0 700 400">
      <rect class="card__bg" width="700" height="400" role="img" aria-label="Pink background with a faint tone-on-tone damask pattern"/>
      <path class="frame-band" d="M105,58 H245 C285,58 300,36 350,36 C400,36 415,58 455,58 H595 A46,46 0 0 0 641,104 V160 C641,185 655,190 655,200 C655,210 641,215 641,240 V296 A46,46 0 0 0 595,342 H455 C415,342 400,364 350,364 C300,364 285,342 245,342 H105 A46,46 0 0 0 59,296 V240 C59,215 45,210 45,200 C45,190 59,185 59,160 V104 A46,46 0 0 0 105,58 Z"/>
      <g class="contact-icons" transform="translate(352 0)">
        <line class="icon-stroke" x1="0" y1="148" x2="0" y2="282" stroke-width="1.5"/>
        <rect x="-10" y="160" width="20" height="16" fill="#fff"/>
        <path class="icon-fill" d="M-8,163 C-8,161 -6,160 -4,161 L-2,165 C-1,167 -3,168 -3,169 C-2,171 0,173 2,174 C3,174 4,172 6,173 L9,175 C10,177 8,179 6,179 C-2,179 -8,172 -8,163 Z"/>
        <rect x="-10" y="201" width="20" height="20" fill="#fff"/>
        <circle class="icon-stroke" cx="0" cy="211" r="8" stroke-width="1.5"/>
        <ellipse class="icon-stroke" cx="0" cy="211" rx="3.5" ry="8" stroke-width="1.2"/>
        <line class="icon-stroke" x1="-8" y1="211" x2="8" y2="211" stroke-width="1.2"/>
        <rect x="-10" y="244" width="20" height="18" fill="#fff"/>
        <rect class="icon-fill" x="-8" y="247" width="16" height="12"/>
        <path d="M-8,247 L0,254 L8,247" fill="none" stroke="#fff" stroke-width="1.2"/>
      </g>
    </svg>

    <div class="social" aria-label="Social profiles">
      <span class="social__item"><span class="social__dot"></span>Chatterbook</span>
      <span class="social__item"><span class="social__dot"></span>Pipsqueak</span>
    </div>

    <div class="identity">
      <p class="identity__name">Danielle Whitcombe</p>
      <p class="identity__role">Photography</p>
    </div>

    <ul class="contact">
      <li class="contact__item">0438 562 073</li>
      <li class="contact__item">www.daniellewhitcombe.com.au</li>
      <li class="contact__item">photos@daniellewhitcombe.com.au</li>
    </ul>
  </section>

</main>
</body>
</html>
```